Tarnby Group letterhead

Hi,

I need a letterhead template created for our business. This should be done in word format and A4 size. The images need to not move in the template ie when I am adding writing in etc. and should flow on when I get to a second page.

I have attached our logo templates below.

Other details to include on the letterhead somewhere are:

0438 915 267
Max@Tarnbyelectrical.example.au
PO Box 817 Marrowvale NSW 2190
ABN: 57 318 962 407

Thanks!

```html
<!DOCTYPE html>
<html lang="en">
<head>
<meta charset="utf-8">
<title>Tarnby Group Letterhead</title>
<link rel="stylesheet" href="https://fonts.googleapis.com/css2?family=Open+Sans:wght@400;600;700&family=Lato:wght@400;700&family=Lexend:wght@400;500&display=swap">
<style>
  :root {
    --orange: #f2530a;
    --ink: #1d1d1d;
    --body: #6d6d6d;
    --muted: #4a4a4a;
    --paper: #ffffff;
    --backdrop: #e9e9eb;
  }
  * { box-sizing: border-box; margin: 0; padding: 0; }
  html, body { width: 999px; height: 1200px; overflow: hidden; }
  body { background: var(--backdrop); font-family: "Open Sans", sans-serif; }
  .letterhead {
    position: absolute; left: 71px; top: 0;
    width: 856px; height: 1200px;
    background: var(--paper);
  }
  .brand {
    position: absolute; left: 62px; top: 49px;
    width: 208px; display: flex; flex-direction: column; align-items: center; gap: 8px;
  }
  .brand-mark { width: 68px; height: 68px; border-radius: 50%; border: 6px solid var(--ink); }
  .brand-name {
    font-family: "Open Sans", sans-serif; font-weight: 700; font-size: 22px; line-height: 28px;
    color: var(--orange); letter-spacing: 1px; text-transform: uppercase; white-space: nowrap;
  }
  .header-rule { position: absolute; left: 57px; top: 210px; width: 737px; height: 10px; }

  .sender-name {
    position: absolute; left: 76px; top: 287px;
    font-size: 22.5px; line-height: 30px; font-weight: 400; color: var(--orange);
  }
  .sender-role {
    position: absolute; left: 77px; top: 318px;
    font-size: 12px; line-height: 16px; color: var(--muted);
  }
  .contact-list { position: absolute; left: 77px; top: 350px; list-style: none; }
  .contact-list li { font-size: 15px; color: var(--muted); line-height: 24px; display: flex; white-space: nowrap; }
  .contact-list b { color: var(--orange); font-weight: 700; width: 30px; }
  .letter-date {
    position: absolute; right: 78px; top: 409px;
    font-size: 15px; line-height: 24px; color: var(--muted);
  }

  .letter-body { position: absolute; left: 77px; top: 486px; width: 701px; }
  .letter-body p {
    font-size: 14.3px; line-height: 22.5px; color: var(--body);
    text-align: justify; margin-bottom: 22.5px;
  }
  .signature {
    position: absolute; left: 94px; top: 849px; width: 120px; height: 75px;
    background: linear-gradient(135deg, #f3f3f3, #e4e4e4); border-radius: 4px;
  }
  .signatory {
    position: absolute; left: 77px; top: 940px; line-height: 28px;
    font-family: "Lexend", sans-serif; font-size: 21px; font-weight: 400; color: var(--ink);
  }
  .footer {
    position: absolute; left: 57px; right: 28px; top: 1127px;
    display: flex; align-items: center; gap: 12px;
    font-family: "Lato", sans-serif; font-size: 12.5px; line-height: 18px; color: var(--ink); white-space: nowrap;
  }
  .footer-item { display: flex; align-items: center; gap: 5px; }
  .footer-item svg { width: 16px; height: 16px; flex: none; }
  .footer-abn { margin-left: auto; }
  .footer-abn b { color: var(--orange); font-weight: 700; }
  .footer-rule { position: absolute; left: 0; right: 0; top: 1150px; height: 1.5px; background: var(--ink); }
</style>
</head>
<body>
<main class="letterhead">
  <header class="brand">
    <span class="brand-mark"></span>
    <span class="brand-name">Tarnby Group</span>
  </header>

  <svg class="header-rule" viewBox="0 0 737 10" aria-hidden="true">
    <polygon points="0,0 235,0 242,10 0,10" fill="#f2530a"/>
    <line x1="242" y1="9.3" x2="737" y2="9.3" stroke="#1d1d1d" stroke-width="1.3"/>
  </svg>

  <h1 class="sender-name">James Doe</h1>
  <p class="sender-role">Chief Director</p>
  <ul class="contact-list">
    <li><b>A :</b>2715 Corbel Avenue, Fenwick 30418</li>
    <li><b>W :</b>www.companywebsite.example</li>
    <li><b>P :</b>+00 123 456 78</li>
    <li><b>M :</b>companyname@mailbox.example</li>
  </ul>

  <p class="letter-date">12 December, 2024</p>

  <article class="letter-body">
    <p>Lorem ipsum dolor sit amet, consectetuer adipiscing elit, sed diam nonummy nibh euismod tincidunt ut laoreet dolore magna aliquam erat volutpat. Ut wisi enim ad minim veniam, quis nostrud exerci tation ullamcorper suscipit lobortis nisl ut aliquip ex ea commodo consequat. Duis autem vel eum iriure dolor in hendrerit in vulputate velit esse molestie consequat, vel illum dolore eu feugiat nulla facilisis at vero eros et accumsan et iusto odio dignissim qui blandit praesent luptatum zzril delenit augue duis dolore te feugait nulla facilisi.</p>
    <p>Lorem ipsum dolor sit amet, cons ectetuer adipiscing elit, sed diam nonummy nibh euismod tincidunt ut laoreet dolore magna aliquam erat volutpat. Ut wisi enim ad minim veniam, quis nostrud exerci tation ullamcorper suscipit lobortis nisl ut aliquip ex ea commodo consequat.</p>
    <p>Lorem ipsum dolor sit amet, consectetuer adipiscing elit, sed diam nonummy nibh euismod tincidunt ut laoreet dolore magna aliquam eratveniam, quis nostrud exerci tation ullamcorper suscipit lobortis nisl ut aliquip ex ea commodo consequat. Lorem ipsum dolor sit zamet, consectetuer adipiscing elit, sed diam nonummy nibh euismod tincidunt.</p>
  </article>

  <div class="signature" role="img" aria-label="Handwritten signature"></div>
  <p class="signatory">Mr. Jone Smith</p>

  <footer class="footer">
    <span class="footer-item">
      <svg viewBox="0 0 16 16" aria-hidden="true"><rect width="16" height="16" rx="2" fill="#f2530a"/><path d="M5 3.5l1.6 2.2-1 1.2c.6 1.4 1.6 2.4 3 3l1.2-1 2.2 1.6-.9 1.8C7.6 12.2 3.8 8.4 3.7 4.4z" fill="#fff"/></svg>
      0438 915 267
    </span>
    <span class="footer-item">
      <svg viewBox="0 0 16 16" aria-hidden="true"><rect width="16" height="16" rx="2" fill="#f2530a"/><rect x="3" y="4.5" width="10" height="7" fill="none" stroke="#fff" stroke-width="1.1"/><path d="M3 4.5l5 4 5-4M3 11.5l3.6-3.6M13 11.5L9.4 7.9" fill="none" stroke="#fff" stroke-width="1"/></svg>
      Max@Tarnbyelectrical.example.au
    </span>
    <span class="footer-item">
      <svg viewBox="0 0 16 16" aria-hidden="true"><rect width="16" height="16" rx="2" fill="#f2530a"/><path d="M8 13.2S4.4 9.2 4.4 6.6a3.6 3.6 0 017.2 0c0 2.6-3.6 6.6-3.6 6.6z" fill="#fff"/><circle cx="8" cy="6.6" r="1.4" fill="#f2530a"/></svg>
      PO Box 817 Marrowvale NSW 2190
    </span>
    <span class="footer-abn"><b>ABN:</b> 57 318 962 407</span>
  </footer>
  <div class="footer-rule"></div>
</main>
</body>
</html>
```